Creating a label for germicidal disposable wipes.

I need to create a label to put on our containers of germicidal disposable wipes. I am attaching an example of another germicidal wipe that I would like a similar format but more customized to look like my companies.

```html
<!DOCTYPE html>
<html lang="en">
<head>
<meta charset="utf-8">
<title>KVR Summit Large Wipe Label</title>
<link rel="stylesheet" href="https://fonts.googleapis.com/css2?family=Roboto+Condensed:ital,wght@0,400;0,500;0,700;1,400&display=swap">
<style>
  :root {
    --navy: #2b2d84;
    --navy-deep: #26287a;
    --green: #2fb34a;
    --grey: #6d6e71;
    --grey-dark: #4a4a4f;
    --ink: #2a2c6a;
    --white: #ffffff;
    --stage: #ececef;
  }
  * { box-sizing: border-box; margin: 0; padding: 0; }
  html, body { width: 1200px; height: 718px; overflow: hidden; }
  body {
    background: var(--stage);
    font-family: "Roboto Condensed", "Arial Narrow", sans-serif;
    position: relative;
  }
  .label {
    position: absolute;
    left: 228px; top: 39px;
    width: 744px; height: 640px;
    background: var(--white);
    box-shadow: 0 6px 18px rgba(0,0,0,.18);
    overflow: hidden;
  }
  .front { position: absolute; left: 0; top: 0; width: 495px; height: 640px; }

  .brand { position: absolute; left: 46px; top: 44px; }
  .brand-row { display: flex; align-items: center; gap: 10px; }
  .brand-dot { width: 40px; height: 40px; border-radius: 50%; background: var(--navy); }
  .brand-name { font-size: 58px; font-weight: 700; color: var(--grey-dark); line-height: 1; letter-spacing: 1px; }
  .brand-division { font-size: 15px; color: var(--grey-dark); letter-spacing: 1px; margin: 2px 0 0 88px; }
  .brand-full { font-size: 15.5px; font-weight: 700; color: var(--green); letter-spacing: .3px; }

  .product {
    position: absolute; left: 347px; top: 0; width: 148px; height: 152px;
    background: linear-gradient(180deg, var(--green) 0%, #2a7a6a 45%, var(--navy) 80%);
    border-bottom-left-radius: 22px;
    color: var(--white); text-align: center;
    overflow: hidden;
  }
  .product-name { font-weight: 700; font-size: 40px; line-height: 1; margin-top: 46px; white-space: nowrap; }
  .product-size { font-size: 16px; margin-top: 14px; letter-spacing: .5px; }

  .icons { position: absolute; left: 46px; top: 168px; width: 365px; height: 140px; }
  .icons-line { position: absolute; left: 40px; right: 40px; top: 49px; height: 3px; background: var(--grey); }
  .icon { position: absolute; top: 0; width: 100px; text-align: center; }
  .icon-disc {
    width: 100px; height: 100px; border-radius: 50%;
    background: var(--grey); border: 4px solid var(--white); outline: 3px solid var(--grey);
    color: var(--white); display: flex; flex-direction: column; align-items: center; justify-content: center;
  }
  .icon-num { font-size: 52px; font-weight: 700; line-height: .9; }
  .icon-unit { font-size: 12px; font-weight: 700; letter-spacing: .5px; }
  .icon-caption { font-size: 12px; color: var(--grey-dark); margin-top: 12px; white-space: nowrap; margin-left: -20px; width: 140px; }

  .claim { position: absolute; left: 46px; top: 318px; font-size: 15px; color: var(--ink); font-weight: 500; letter-spacing: .2px; }
  .ingredients-title { position: absolute; left: 46px; top: 350px; font-size: 16px; font-weight: 700; color: var(--green); text-decoration: underline; letter-spacing: .3px; }
  .ingredients { position: absolute; left: 46px; top: 379px; width: 387px; list-style: none; }
  .ingredients li { display: flex; font-size: 15px; color: var(--grey-dark); line-height: 21px; }
  .ingredients .dots { flex: 1; border-bottom: 2px dotted var(--grey); margin: 0 4px 6px; }
  .note { position: absolute; left: 46px; top: 474px; font-size: 13px; font-style: italic; color: var(--grey-dark); }

  .warning-band {
    position: absolute; left: 0; top: 495px; width: 495px; height: 112px;
    background: var(--navy-deep); padding: 6px 0 0 48px; color: var(--white);
  }
  .keep-out { font-size: 20px; color: var(--green); font-weight: 500; letter-spacing: .3px; }
  .warning-row { display: flex; align-items: center; gap: 8px; margin-top: 1px; }
  .warning-word { font-weight: 700; font-size: 30px; line-height: 1; letter-spacing: .3px; }
  .warning-small { font-size: 11.5px; line-height: 1.05; }
  .contents { font-size: 19px; margin-top: 2px; }
  .contents small { font-size: 11px; }
  .net-weight { font-size: 11px; margin-top: 1px; }

  .back {
    position: absolute; left: 495px; top: 0; width: 249px; height: 640px;
    background: linear-gradient(90deg, var(--green) 0%, #21817a 35%, var(--navy) 75%);
    color: var(--white); padding: 38px 22px 0 25px;
  }
  .back-title { font-size: 16px; font-weight: 500; margin-bottom: 10px; }
  .back p { font-size: 9.8px; line-height: 1.3; font-weight: 500; margin-bottom: 12px; }
  .back p strong { font-size: 13px; font-weight: 500; }
</style>
</head>
<body>
  <main class="label">
    <section class="front">
      <div class="brand">
        <div class="brand-row">
          <span class="brand-dot"></span>
          <span class="brand-name">KVR</span>
        </div>
        <div class="brand-division">HAZARDOUS DIVISION</div>
        <div class="brand-full">KESTREL VALE REMEDIATION</div>
      </div>

      <div class="product">
        <div class="product-name">SUMMIT</div>
        <div class="product-size">LARGE WIPE</div>
      </div>

      <div class="icons">
        <div class="icons-line"></div>
        <div class="icon" style="left:0">
          <div class="icon-disc"><span class="icon-num">2</span><span class="icon-unit">MINUTES</span></div>
          <div class="icon-caption">DISINFECTS IN</div>
        </div>
        <div class="icon" style="left:134px">
          <div class="icon-disc" role="img" aria-label="Icon of hands wiping, crossed out"></div>
          <div class="icon-caption">NOT A SKIN OR BABY WIPE</div>
        </div>
        <div class="icon" style="left:263px">
          <div class="icon-disc" role="img" aria-label="Icon of a toilet, do not flush"></div>
          <div class="icon-caption">DO NOT FLUSH</div>
        </div>
      </div>

      <div class="claim">BACTERICIDAL, TUBERCULOCIDAL, AND VIRUCIDAL * IN 2 MINUTES</div>
      <div class="ingredients-title">ACTIVE INGREDIENTS</div>
      <ul class="ingredients">
        <li><span>BACTERICIDAL,</span><span class="dots"></span><span>05%</span></li>
        <li><span>TUBERCULOCIDAL</span><span class="dots"></span><span>05%</span></li>
        <li><span>VIRUCIDAL</span><span class="dots"></span><span>05%</span></li>
        <li><span>BACTERICIDAL,</span><span class="dots"></span><span>05%</span></li>
      </ul>
      <div class="note">Does not icludie the weight of thr wipe</div>

      <div class="warning-band">
        <div class="keep-out">KEEP OUT OF REACH OF CHILDREN</div>
        <div class="warning-row">
          <span class="warning-word">WARNING</span>
          <span class="warning-small">See back panel for additional<br>precautionary statements</span>
        </div>
        <div class="contents">Contains: 160 wipes <small>6x6.75in (15.2 x 17.1cm)</small></div>
        <div class="net-weight">Net Wt. 1 lb 13 oz (833g)</div>
      </div>
    </section>

    <section class="back">
      <h2 class="back-title">Title Here:</h2>
      <p><strong>Lorem ipsum</strong> dolor sit amet, consectetuer adipiscing elit, sed diam nonummy nibh euismod tincidunt ut laoreet dolore magna aliquam erat volutpat. Ut wisi enim ad minim veniam, quis nostrud exerci tation ullamcorper suscipit lobortis nisl ut aliquip ex ea commodo consequat. Duis autem vel eum iriure dolor in hendrerit in vulputate velit esse molestie consequat, vel illum dolore eu feugiat nulla facilisis at vero eros et accumsan et iusto odio dignissim qui blandit praesent luptatum zzril delenit augue duis dolore te feugait nulla facilisi.</p>
      <p><strong>Lorem ipsum</strong> dolor sit amet, cons ectetuer adipiscing elit, sed diam nonummy nibh euismod tincidunt ut laoreet dolore magna aliquam erat volutpat. Ut wisi enim ad minim veniam, quis nostrud exerci tation ullamcorper suscipit lobortis nisl ut aliquip ex ea commodo consequat. Lorem ipsum dolor sit amet, consectetuer adipiscing elit, sed diam nonummy nibh euismod tincidunt ut laoreet dolore magna aliquam erat volutpat. Ut wisi enim ad minim veniam, quis nostrud exerci tation ullamcorper suscipit lobortis nisl ut aliquip ex ea commodo consequat. Duis autem vel eum iriure dolor in hendrerit in vulputate velit esse molestie consequat, vel illum dolore eu feugiat nulla facilisis at vero eros et accumsan et iusto odio dignissim qui blandit praesent luptatum zzril delenit augue duis dolore te feugait nulla facilisi.</p>
      <p><strong>Lorem ipsum</strong> dolor sit amet, cons ectetuer adipiscing elit, sed diam nonummy nibh euismod tincidunt ut laoreet dolore magna aliquam erat volutpat. Ut wisi enim ad minim veniam, quis nostrud exerci tation ullamcorper suscipit lobortis nisl ut aliquip ex ea commodo consequat.</p>
    </section>
  </main>
</body>
</html>
```